Company Playbill Advertisement Design

I own a production company that provides audio,lighting,video, and other production services to events and conventions. I am sponsoring a event and they are giving me a full page ad in the playbill. It needs to be Full Page (Full Bleed) Trim Area: 5.5” x 8.5” Image Area: 5” x 8”. I would like the design to include photos, information about my company, and my logo in a professional presentation to lure potential clients to contact us. We are a production company so it needs to be something that catches your eye but professional.

Target Market(s)

Companies looking for production services. Our customer is mainly a professional person looking for services. We are not a DJ company so our market is a bit smaller.

Industry/Entity Type

Events

Requirements
Must have
• Company phone number is 555-704-2981, website is www.brivanstagecrew.example. Company Logo, photos of events.
• Accepted Ad Formats: .jpg, .pdf., .eps. Full Color Minimum 300 dpi All Fonts Outlined. It needs to be Full Page (Full Bleed) Trim Area: 5.5” x 8.5” Image Area: 5” x 8”.
Nice to have
• Creative design that catches someone eye. We are a creative company so we want our ad to reflect that.

```html
<!DOCTYPE html>
<html lang="en">
<head>
<meta charset="utf-8">
<title>Brivan Stage Crew – Playbill Ad</title>
<link href="https://fonts.googleapis.com/css2?family=Open+Sans:wght@400;700;800&display=swap" rel="stylesheet">
<style>
  :root {
    --ink: #111111;
    --paper: #ffffff;
    --band: #141414;
    --accent: #e0141b;
    --text-body: #222222;
    --photo-deep: #1a0f2e;
    --photo-pink: #c2357a;
    --photo-blue: #3a7fc4;
    --photo-warm: #d8843c;
  }
  * { margin: 0; padding: 0; box-sizing: border-box; }
  html, body { width: 777px; height: 1200px; overflow: hidden; background: var(--paper); }
  body { font-family: "Open Sans", Arial, sans-serif; color: var(--ink); }
  .ad { position: relative; width: 777px; height: 1200px; overflow: hidden; background: var(--paper); }

  .hero-photo {
    position: absolute; left: 0; top: 0; width: 777px; height: 580px;
    background:
      radial-gradient(ellipse at 70% 35%, rgba(58,127,196,0.75), transparent 55%),
      radial-gradient(ellipse at 15% 25%, rgba(194,53,122,0.8), transparent 55%),
      radial-gradient(ellipse at 55% 95%, rgba(216,132,60,0.7), transparent 50%),
      linear-gradient(180deg, var(--photo-deep), #2a1230 70%, #3a1c1a);
  }
  .headline {
    position: absolute; left: 56px; top: 58px;
    font-weight: 800; font-size: 29.5px; line-height: 35px; color: var(--paper);
    text-transform: uppercase; letter-spacing: 0.3px;
  }
  .headline span { display: inline-block; background: rgba(0,0,0,0.55); padding: 0 6px; }
  .headline .period { color: var(--accent); background: none; margin-top: 4px; }

  .brand-top {
    position: absolute; right: 58px; top: 64px;
    font-weight: 800; font-size: 22px; color: var(--paper); letter-spacing: 0.5px;
  }

  .who-band {
    position: absolute; left: 0; top: 580px; width: 777px; height: 80px;
    background: var(--band); color: var(--paper);
  }
  .who-label {
    position: absolute; left: 50px; top: 66px; transform: rotate(-90deg); transform-origin: left top;
    font-weight: 800; line-height: 1;
  }
  .who-label b { display: block; font-size: 18px; }
  .who-label small { display: block; font-size: 9px; font-weight: 800; }
  .who-text { position: absolute; left: 114px; top: 12px; width: 600px; font-size: 14px; line-height: 18px; }

  .what-title {
    position: absolute; left: 54px; top: 680px;
    font-weight: 800; font-size: 42px; line-height: 1; display: flex; align-items: center;
  }
  .what-title .stack { font-size: 15px; line-height: 15px; margin: 0 6px 0 10px; }

  .services { position: absolute; top: 744px; }
  .services.left { left: 54px; }
  .services.right { right: 54px; text-align: right; }
  .service { height: 62px; }
  .service h3 { font-weight: 700; font-size: 22px; line-height: 24px; text-transform: uppercase; }
  .service p { font-size: 13px; line-height: 14.5px; color: var(--text-body); }

  .brand-bottom {
    position: absolute; left: 64px; top: 1120px; display: flex; align-items: center; gap: 8px;
    font-weight: 800; font-size: 24px; color: var(--ink);
  }
  .brand-bottom .mark { width: 14px; height: 14px; background: var(--accent); }

  .contact { position: absolute; right: 54px; top: 1110px; text-align: right; font-weight: 700; font-size: 21px; line-height: 24px; }
</style>
</head>
<body>
<div class="ad">
  <div class="hero-photo" role="img" aria-label="Festival crowd under stage lights with confetti falling"></div>

  <h1 class="headline">
    <span>The best sales,</span><br>
    <span>production, and</span><br>
    <span>rental company</span><br>
    <span>you need in</span><br>
    <span>Central Florida.</span><br>
    <span class="period">Period.</span>
  </h1>

  <div class="brand-top">Brivan Stage Crew</div>

  <section class="who-band">
    <div class="who-label"><b>WHO</b><small>WE ARE?</small></div>
    <p class="who-text">Brivan Stage Crew or BSC is your source for events, sales, production services, and entertainment in the Central Florida area. We can meet your needs in a hurry. We excel in the live event category with over 14 years experience in shows and festivals.</p>
  </section>

  <h2 class="what-title">WHAT <span class="stack">WE<br>DO</span>?</h2>

  <div class="services left">
    <div class="service"><h3>Audio Services</h3><p>BSC has some of the best<br>audio gear so you can be heard</p></div>
    <div class="service"><h3>Lighting Services</h3><p>We have the latest in automated<br>lighting fixtures</p></div>
    <div class="service"><h3>Event Video</h3><p>BSC has a full line of LED walls<br>and projectors to fit any event and budget</p></div>
    <div class="service"><h3>Effects</h3><p>Fog, Haze, Snow, Cryo C02, Confetti,<br>Pyro, Low Lying Fog</p></div>
    <div class="service"><h3>Rigging</h3><p>We can elevate your event by providing<br>trussing, motors, or towers to hang<br>anything that needs to be put up</p></div>
  </div>

  <div class="services right">
    <div class="service"><h3>Mobile / Deck Staging</h3><p>We can provide any size mobile or<br>deck stage for your needs</p></div>
    <div class="service"><h3>Event Management</h3><p>We can take your event ideas<br>and make them a success</p></div>
    <div class="service"><h3>Sales and Install</h3><p>We provide the best gear for any situation<br>and will train you on how to use it</p></div>
    <div class="service"><h3>Equipment Rentals</h3><p>BSC is a great source for rental gear.<br>Audio, Lighting, Video, LED Wall, Staging</p></div>
    <div class="service"><h3>Equipment Rentals</h3><p>We partner with the award-winning team<br>at Lumen Arc Visual Studio on all video<br>and film production services</p></div>
  </div>

  <div class="brand-bottom"><span class="mark"></span>Brivan Stage Crew</div>

  <div class="contact">555-704-2981<br>www.brivanstagecrew.example</div>
</div>
</body>
</html>
```